Bright Path Mentors Needs A New Website Design

We need a 8 page website designed for "Bright Path Mentors .ca" similar in design to: "quill ridge learning .com".

The winner/successful candidate on the home page will be asked to complete the following inner pages to complete the project:

About Us
Philosophy
How We Work
Work With Us
Blog
Find A Tutor
Contact

Target Market(s)

Tutoring business clients/children

Industry/Entity Type

Education

Number of Pages Required

5+ page

Font styles to use
Sans Serif

Requirements
Must have
• The attached logo included of course. Similar design to the design provided above in the brief. Clear high quality high resolution images of children in school settings.

```html
<!DOCTYPE html>
<html lang="en">
<head>
<meta charset="utf-8">
<title>Bright Path Mentors</title>
<link href="https://fonts.googleapis.com/css2?family=Lato:wght@300;400;700;900&display=swap" rel="stylesheet">
<style>
:root{
  --teal:#1c8e9f;
  --teal-dark:#157683;
  --yellow:#f1c21b;
  --green:#10c04c;
  --green-text:#17b34a;
  --dark:#333333;
  --ink:#2b2b2b;
  --muted:#777;
  --cream:#fdf6e4;
  --red:#e8473d;
  --white:#ffffff;
}
*{box-sizing:border-box;margin:0;padding:0}
html,body{width:1200px;height:4000px;overflow:hidden}
body{font-family:'Lato',sans-serif;color:var(--ink);background:var(--white);position:relative}

/* header */
.site-header{position:absolute;left:0;top:0;width:1200px;height:100px;background:var(--white)}
.nav{position:absolute;top:40px;display:flex;gap:48px;font-size:15px;font-weight:700;letter-spacing:.5px;color:var(--ink)}
.nav-left{left:110px}
.nav-right{left:742px}
.brand{position:absolute;left:550px;top:18px;width:100px;text-align:center}
.brand-mark{width:34px;height:34px;border-radius:50%;background:var(--teal);margin:0 auto 4px}
.brand-name{font-size:13px;font-weight:900;color:var(--teal-dark);line-height:1.1}

/* hero */
.hero{position:absolute;left:0;top:100px;width:1200px;height:700px;background:linear-gradient(110deg,#3f4a55 0%,#8a8f93 35%,#c9b9a8 60%,#aeb2b5 100%)}
.hero-card{position:absolute;left:88px;top:161px;width:440px;height:360px;background:rgba(255,255,255,.92);padding:42px 40px 30px}
.hero-kicker{font-size:17px;letter-spacing:.5px;color:var(--ink)}
.hero-title{font-size:31px;font-weight:700;line-height:1.25;margin-top:14px;color:var(--ink);text-transform:uppercase;white-space:nowrap}
.hero-title .hl{color:var(--green-text)}
.hero-text{font-size:14px;line-height:1.6;color:#555;margin-top:16px}
.hero-text a{color:var(--teal);font-weight:700;text-decoration:none}

/* intro */
.intro{position:absolute;left:0;top:800px;width:1200px;height:461px;background:var(--white)}
.section-title{font-size:26px;font-weight:900;letter-spacing:.5px;text-transform:uppercase;text-align:center;display:flex;align-items:center;justify-content:center;gap:24px}
.section-title .dot{width:12px;height:12px;background:currentColor;transform:rotate(45deg)}
.intro .section-title{position:absolute;top:78px;width:100%;color:var(--green-text)}
.intro-photo{position:absolute;left:93px;top:165px;width:307px;height:208px;background:linear-gradient(135deg,#3d6b3a,#a07f4e 55%,#d8c49a);border:6px solid #eee}
.intro-text{position:absolute;left:453px;top:160px;width:662px;font-size:12px;line-height:1.6;color:#8a8a8a}
.intro-quote{position:absolute;left:453px;top:293px;width:662px;height:80px;background:var(--yellow);color:var(--white);font-size:15px;font-style:italic;font-weight:700;line-height:1.5;padding:14px 20px}
.intro-name{position:absolute;left:483px;top:382px;font-size:16px;font-weight:700;letter-spacing:1px;color:#8a8a8a}

/* features */
.features{position:absolute;left:0;top:1261px;width:1200px;height:318px;background:var(--teal)}
.feature-box{position:absolute;top:38px;width:280px;height:240px;border:2px solid rgba(255,255,255,.85);border-radius:6px;text-align:center;color:var(--white)}
.feature-box h3{font-weight:400;font-size:27px;line-height:1.05;text-transform:uppercase;margin-top:34px}
.feature-box .rule{width:220px;height:2px;background:rgba(255,255,255,.8);margin:26px auto 22px}
.feature-box .btn{display:inline-block;background:var(--white);color:var(--teal);font-size:13px;font-weight:900;padding:10px 18px;border-radius:3px}

/* why */
.why{position:absolute;left:0;top:1579px;width:1200px;height:674px;background:var(--yellow)}
.why .section-title{position:absolute;top:48px;width:100%;color:var(--white);font-weight:700;font-size:32px}
.why-card{position:absolute;width:490px;height:152px;background:var(--white);padding:20px}
.why-inner{width:100%;height:100%;background:var(--cream);display:flex;align-items:center;padding:0 16px}
.why-icon{flex:0 0 84px;height:84px;border:3px solid var(--yellow);border-radius:50%;background:var(--white);display:flex;align-items:center;justify-content:center}
.why-sep{width:2px;height:84px;background:var(--yellow);margin:0 18px}
.why-copy h4{font-size:17px;font-weight:700;color:var(--ink)}
.why-copy p{font-size:11.5px;line-height:1.45;color:#666;margin-top:6px}

/* testimonials */
.testimonials{position:absolute;left:0;top:2253px;width:1200px;height:622px;background:linear-gradient(180deg,#1a8494,#1f97a8)}
.testimonials .section-title{position:absolute;top:68px;width:100%;color:var(--white);font-size:26px}
.quote-card{position:absolute;top:166px;width:493px;height:256px;background:var(--white);text-align:center;padding:32px 36px}
.quote-card::after{content:"";position:absolute;left:50%;bottom:-16px;margin-left:-16px;border-left:16px solid transparent;border-right:16px solid transparent;border-top:16px solid var(--white)}
.quote-mark{width:48px;height:48px;border-radius:50%;background:var(--teal);margin:0 auto 22px;display:flex;align-items:center;justify-content:center}
.quote-card p{font-size:12.5px;line-height:1.6;color:#666;text-transform:uppercase}
.avatar{position:absolute;top:456px;width:62px;height:62px;border-radius:50%;background:linear-gradient(135deg,#3a4a45,#8a7a6a);border:3px solid var(--white)}
.avatar-name{position:absolute;top:532px;width:160px;text-align:center;font-size:13px;font-weight:900;color:var(--white)}

/* stats */
.stats{position:absolute;left:0;top:2875px;width:1200px;height:280px;background:var(--dark);color:var(--white)}
.stat{position:absolute;top:38px;width:240px;text-align:center}
.stat .num{font-size:50px;font-weight:700;line-height:1.1}
.stat .rule{width:200px;height:3px;background:var(--white);margin:10px auto 16px}
.stat .label{font-size:27px;font-weight:300;line-height:1.1;text-transform:uppercase}
.stat .sub{font-size:14px;color:#ccc;margin-top:10px}

/* contact */
.contact{position:absolute;left:0;top:3155px;width:1200px;height:525px;background:linear-gradient(90deg,#cfcfcf,#e4e4e4 55%,#d6d6d6)}
.contact-panel{position:absolute;left:0;top:0;width:600px;height:525px;background:rgba(70,70,70,.55)}
.contact h2{position:absolute;left:128px;top:72px;font-size:25px;font-weight:700;color:var(--white)}
.field{position:absolute;background:var(--white);font-size:14px;color:#666;padding:12px 14px}
.submit{position:absolute;left:128px;top:290px;width:432px;height:44px;background:var(--red);color:var(--white);font-size:20px;font-weight:700;text-align:center;line-height:44px}
.info{position:absolute;left:128px;display:flex;align-items:center;gap:18px;font-size:14px;color:var(--white)}

/* footer */
.site-footer{position:absolute;left:0;top:3680px;width:1200px;height:320px;background:var(--green);color:var(--white)}
.foot-head{position:absolute;font-size:19px;font-weight:900;text-transform:uppercase}
.foot-list{position:absolute;list-style:none;font-size:12.5px;line-height:19.5px}
.foot-list li::before{content:"";display:inline-block;width:5px;height:5px;background:var(--white);margin-right:10px;vertical-align:middle}
.page-widget{position:absolute;left:928px;top:48px;width:180px;height:220px;background:var(--white);padding:10px;color:var(--ink)}
.page-widget .cover{height:100px;background:linear-gradient(135deg,#c9c0b4,#8c7f72)}
.page-widget .name{font-size:14px;font-weight:700;margin-top:8px}
.page-widget .like{display:inline-block;margin-top:8px;background:#eee;border:1px solid #ccc;font-size:11px;padding:3px 8px}
.page-widget .note{font-size:11px;color:#666;margin-top:8px;line-height:1.3}
</style>
</head>
<body>

<header class="site-header">
  <nav class="nav nav-left"><span>ABOUT US</span><span>ACADEMIC TUTORING</span><span>TEST PREP</span></nav>
  <div class="brand"><div class="brand-mark"></div><div class="brand-name">Bright Path Mentors</div></div>
  <nav class="nav nav-right"><span>PRICING</span><span>OUR TUTORS</span><span>CONTACT US</span></nav>
</header>

<section class="hero" role="img" aria-label="Photo of a young girl with glasses using a tablet in a classroom">
  <div class="hero-card">
    <div class="hero-kicker">ITS TIME TO LEARN</div>
    <h1 class="hero-title">Your <span class="hl">First Step</span> to<br><span class="hl">Quality Education</span></h1>
    <p class="hero-text">Illo inventore veritatis et quasi architecto beatae vitae dicta sunt explicabo. Nemo enim ipsam voluptatem quia voluptas sit aspernatur aut odit aut fugit, sed quia consequuntur magni dolores eos qui ratione voluptatem sequi nesciunt, quis dolor sit amet <a>Read More</a></p>
  </div>
</section>

<section class="intro">
  <h2 class="section-title"><span class="dot"></span>Best Home Tutoring<span class="dot"></span></h2>
  <div class="intro-photo" role="img" aria-label="Photo of a smiling student waving in a classroom"></div>
  <p class="intro-text">Inventore veritatis et quasi architecto beatae vitae dicta sunt explicabo. Nemo enim ipsam voluptatem quia voluptas sit aspernatur aut odit aut fugit, sed quia consequuntur magni dolores eos qui ratione voluptatem sequi nesciunt. Neque porro quisquam est, qui dolorem ipsum quia dolor sit amet, consectetur, adipisci velit, sed quia non numquam eius modi tempora incidunt ut labore et dolore magnam aliquam quaerat voluptatem. Ut enim ad minima veniam, quis nostrum exercitationem ullam corporis suscipit laboriosam, nisi ut aliquid ex ea commodi consequatur? Quis autem vel eum iure reprehenderit qui in ea voluptate velit esse quam nihil molestiae consequatur, vel illum.</p>
  <div class="intro-quote">Lorem ipsum dolor sit amet, consectetur adipiscing elit, sed do eiusmod tempor incididunt ut labore et dolore magna aliqua. Ut enim ad minim veniam, quis</div>
  <div class="intro-name">MARA QUINN</div>
</section>

<section class="features">
  <div class="feature-box" style="left:88px"><h3>Making<br>Students Love<br>Their Studies</h3><div class="rule"></div><span class="btn">VIEW REVIEWS</span></div>
  <div class="feature-box" style="left:461px"><h3>Highly<br>Professional<br>Tutoring</h3><div class="rule"></div><span class="btn">OUR WORK</span></div>
  <div class="feature-box" style="left:834px"><h3>Best<br>Tutors<br>Community</h3><div class="rule"></div><span class="btn">FIND TUTOR</span></div>
</section>

<section class="why">
  <h2 class="section-title">WHY BRIGHT PATH MENTORS?</h2>

  <div class="why-card" style="left:88px;top:122px"><div class="why-inner">
    <div class="why-icon"><svg width="40" height="32" viewBox="0 0 40 32" fill="none" stroke="#333" stroke-width="2.5"><rect x="2" y="2" width="36" height="24" rx="2"/><line x1="8" y1="10" x2="22" y2="10"/><line x1="8" y1="16" x2="18" y2="16"/><circle cx="30" cy="16" r="4"/></svg></div>
    <div class="why-sep"></div>
    <div class="why-copy"><h4>Certified Tutors</h4><p>Sed ut perspiciatis unde omnis iste natus error sit voluptatem accusantium doloremque laudantium, totam rem aperiam, eaque ipsa quae ab illo inventore veritatis et quasi architecto beatae vitae dicta sunt explicabo.</p></div>
  </div></div>

  <div class="why-card" style="left:622px;top:122px"><div class="why-inner">
    <div class="why-icon"><svg width="40" height="40" viewBox="0 0 40 40" fill="none" stroke="#333" stroke-width="3"><circle cx="20" cy="20" r="17"/><polyline points="20,9 20,20 28,24"/></svg></div>
    <div class="why-sep"></div>
    <div class="why-copy"><h4>Flexible Hours</h4><p>Sed ut perspiciatis unde omnis iste natus error sit voluptatem accusantium doloremque laudantium, totam rem aperiam, eaque ipsa quae ab illo inventore veritatis et quasi architecto beatae vitae dicta sunt explicabo.</p></div>
  </div></div>

  <div class="why-card" style="left:88px;top:301px"><div class="why-inner">
    <div class="why-icon"><svg width="36" height="38" viewBox="0 0 36 38" fill="#333"><circle cx="18" cy="11" r="9"/><path d="M2 38c0-10 7-16 16-16s16 6 16 16z"/></svg></div>
    <div class="why-sep"></div>
    <div class="why-copy"><h4>Personal Attention</h4><p>Sed ut perspiciatis unde omnis iste natus error sit voluptatem accusantium doloremque laudantium, totam rem aperiam, eaque ipsa quae ab illo inventore veritatis et quasi architecto beatae vitae dicta sunt explicabo.</p></div>
  </div></div>

  <div class="why-card" style="left:622px;top:301px"><div class="why-inner">
    <div class="why-icon"><svg width="40" height="30" viewBox="0 0 40 30" fill="none" stroke="#333" stroke-width="3"><polyline points="2,27 14,15 22,21 36,5"/><polyline points="28,5 36,5 36,13"/></svg></div>
    <div class="why-sep"></div>
    <div class="why-copy"><h4>Top Notch Results</h4><p>Sed ut perspiciatis unde omnis iste natus error sit voluptatem accusantium doloremque laudantium, totam rem aperiam, eaque ipsa quae ab illo inventore veritatis et quasi architecto beatae vitae dicta sunt explicabo.</p></div>
  </div></div>

  <div class="why-card" style="left:355px;top:480px"><div class="why-inner">
    <div class="why-icon"><svg width="38" height="36" viewBox="0 0 38 36" fill="none" stroke="#333" stroke-width="2.5" stroke-linejoin="round"><rect x="2" y="15" width="8" height="19"/><path d="M10 17l8-14c3 0 5 2 4 6l-2 6h12c3 0 5 3 4 5l-3 11c-1 2-2 3-4 3H10z"/></svg></div>
    <div class="why-sep"></div>
    <div class="why-copy"><h4>Best Results Guaranteed</h4><p>Sed ut perspiciatis unde omnis iste natus error sit voluptatem accusantium doloremque laudantium, totam rem aperiam, eaque ipsa quae ab illo inventore veritatis et quasi architecto beatae vitae dicta sunt explicabo.</p></div>
  </div></div>
</section>

<section class="testimonials" aria-label="Client testimonials">
  <h2 class="section-title"><span class="dot"></span>What Our Clients Say<span class="dot"></span></h2>
  <div class="quote-card" style="left:88px">
    <div class="quote-mark"><svg width="22" height="18" viewBox="0 0 22 18" fill="#fff"><path d="M0 18V9C0 3 3 0 8 0v4c-2 0-4 2-4 5h4v9zM12 18V9c0-6 3-9 8-9v4c-2 0-4 2-4 5h4v9z"/></svg></div>
    <p>"Lorem ipsum dolor sit amet, consectetur adipisicing elit, sed do eiusmod tempor incididunt ut labore et dolore magna aliqua. Ut enim ad minim veniam, quis nostrud exercitation ullamco laboris nisi ut aliquip ex ea commodo consequat. Cupidatat non proident, sunt in culpa qui officia deserunt mollit"</p>
  </div>
  <div class="quote-card" style="left:621px">
    <div class="quote-mark"><svg width="22" height="18" viewBox="0 0 22 18" fill="#fff"><path d="M0 18V9C0 3 3 0 8 0v4c-2 0-4 2-4 5h4v9zM12 18V9c0-6 3-9 8-9v4c-2 0-4 2-4 5h4v9z"/></svg></div>
    <p>"Lorem ipsum dolor sit amet, consectetur adipisicing elit, sed do eiusmod tempor incididunt ut labore et dolore magna aliqua. Ut enim ad minim veniam, quis nostrud exercitation ullamco laboris nisi ut aliquip ex ea commodo consequat. Cupidatat non proident, sunt in culpa qui officia deserunt mollit"</p>
  </div>
  <div class="avatar" style="left:303px" role="img" aria-label="Client portrait"></div>
  <div class="avatar-name" style="left:254px">JHON DOU</div>
  <div class="avatar" style="left:836px" role="img" aria-label="Client portrait"></div>
  <div class="avatar-name" style="left:787px">JHON DOU</div>
</section>

<section class="stats">
  <div class="stat" style="left:93px"><div class="num">3,596</div><div class="rule"></div><div class="label">Certified<br>Clients</div><div class="sub">and counting</div></div>
  <div class="stat" style="left:347px"><div class="num">7,544</div><div class="rule"></div><div class="label">Successfull<br>Tests</div><div class="sub">and counting</div></div>
  <div class="stat" style="left:607px"><div class="num">349</div><div class="rule"></div><div class="label">Positions<br>Won</div><div class="sub">and counting</div></div>
  <div class="stat" style="left:861px"><div class="num">58</div><div class="rule"></div><div class="label">Subjects<br>Covered</div><div class="sub">and counting</div></div>
</section>

<section class="contact" role="img" aria-label="Greyscale street map showing office locations">
  <div class="contact-panel"></div>
  <h2>CONTACT US</h2>
  <div class="field" style="left:128px;top:128px;width:205px;height:46px">Name:</div>
  <div class="field" style="left:347px;top:128px;width:213px;height:46px">Email:</div>
  <div class="field" style="left:128px;top:189px;width:432px;height:91px">Message here...</div>
  <div class="submit">SUBMIT</div>
  <div class="info" style="top:370px"><svg width="16" height="22" viewBox="0 0 16 22" fill="#fff"><path d="M8 0a8 8 0 0 1 8 8c0 6-8 14-8 14S0 14 0 8a8 8 0 0 1 8-8zm0 5a3 3 0 1 0 0 6 3 3 0 0 0 0-6z"/></svg>1820 Harbour Lane, Suite 210</div>
  <div class="info" style="top:410px"><svg width="18" height="18" viewBox="0 0 18 18" fill="#fff"><path d="M4 0l3 4-2 3c1 2 3 4 6 6l3-2 4 3-2 4C8 18 0 10 0 2z"/></svg>1-800-555-0142</div>
  <div class="info" style="top:454px"><svg width="20" height="14" viewBox="0 0 20 14" fill="#fff"><path d="M0 0h20v14H0zM2 2l8 6 8-6" stroke="#777" stroke-width="1.5"/></svg>info@brightpathmentors.ca</div>
</section>

<footer class="site-footer">
  <div class="foot-head" style="left:88px;top:38px">Subjects</div>
  <ul class="foot-list" style="left:92px;top:70px"><li>Elementary Tutoring</li><li>Foreign Languages</li><li>Elementary Tutoring</li><li>Foreign Languages</li></ul>
  <div class="foot-head" style="left:88px;top:170px">Locations</div>
  <ul class="foot-list" style="left:92px;top:202px"><li>Toronto</li><li>Toronto</li><li>Toronto</li><li>Toronto</li></ul>
  <ul class="foot-list" style="left:200px;top:202px"><li>Toronto</li><li>Toronto</li><li>Toronto</li><li>Toronto</li></ul>

  <div class="foot-head" style="left:344px;top:38px">Other Subjects</div>
  <ul class="foot-list" style="left:348px;top:70px"><li>Elementary Tutoring</li><li>Elementary Tutoring</li><li>Elementary Tutoring</li><li>Elementary Tutoring</li><li>Elementary Tutoring</li><li>Elementary Tutoring</li><li>Elementary Tutoring</li><li>Elementary Tutoring</li><li>Elementary Tutoring</li><li>Elementary Tutoring</li><li>Elementary Tutoring</li></ul>
  <ul class="foot-list" style="left:516px;top:70px"><li>Elementary Tutoring</li><li>Elementary Tutoring</li><li>Elementary Tutoring</li><li>Elementary Tutoring</li><li>Elementary Tutoring</li><li>Elementary Tutoring</li><li>Elementary Tutoring</li><li>Elementary Tutoring</li><li>Elementary Tutoring</li><li>Elementary Tutoring</li><li>Elementary Tutoring</li></ul>

  <div class="foot-head" style="left:688px;top:38px">Company</div>
  <ul class="foot-list" style="left:692px;top:70px"><li>Elementary Tutoring</li><li>Elementary Tutoring</li><li>Elementary Tutoring</li><li>Elementary Tutoring</li><li>Elementary Tutoring</li><li>Elementary Tutoring</li><li>Elementary Tutoring</li><li>Elementary Tutoring</li><li>Elementary Tutoring</li><li>Elementary Tutoring</li><li>Elementary Tutoring</li></ul>

  <div class="page-widget">
    <div class="cover" role="img" aria-label="Page cover photo"></div>
    <div class="name">Bright Path Mentors</div>
    <span class="like">Like Page</span>
    <div class="note">Be the first of your friends to like this</div>
  </div>
</footer>

</body>
</html>
```